Layout for new page on existing website

We have an existing website (www.brightloomworks.org) and need a new page designing to promote a new product.
The new page needs to be consistent with the existing website look and feel (www.brightloomworks.org) but current persistent elements on the standard page design can be moved/removed from the page to accommodate a new layout necessary for getting all the content laid out in a logical user friendly way.
The content required for the page is attached along with a wireframe mock up that may help understand the expectation, however the wireframe was just created to help me work out what was needed on the page and the layout can be different. A key element is the quality of the design of each of the artifacts (e.g. the panel the embedded video needs to go in, icons etc) and a clear display of the information.
Updates
The website that the new page needs to fit into is www.brightloomworks.org, i will also added the company logo to the brief.
Our Corporate Colours
- Green: #A2FF00
- Cream: #FFFF99
- Yellow: #FFE900
- Grey: #534741
Industry/Entity Type
Product
Look and feel
Each slider illustrates characteristics of the customer's brand and the style your logo design should communicate.

```html
<!DOCTYPE html>
<html lang="en">
<head>
<meta charset="utf-8">
<title>Brightloom Works – Course Management and Booking</title>
<link rel="stylesheet" href="https://fonts.googleapis.com/css2?family=Oswald:wght@400&family=Roboto+Condensed:ital,wght@0,400;0,700;1,400;1,700&family=Open+Sans:wght@600;700&display=swap">
<style>
  :root {
    --grey: #4f423d;
    --grey-dark: #3f3531;
    --green: #a2ff00;
    --cream: #ffff99;
    --yellow: #f8ea32;
    --olive: #8e8c5a;
    --olive-line: #5f5c3e;
    --quote: #e4e9a2;
    --white: #ffffff;
    --heading-ink: #4a3d37;
    --glow: #ffe35c;
  }
  * { box-sizing: border-box; margin: 0; padding: 0; }
  html, body { width: 1045px; height: 1200px; overflow: hidden; }
  body {
    position: relative;
    background: var(--grey);
    font-family: "Roboto Condensed", sans-serif;
    color: var(--white);
  }

  /* Brand */
  .brand {
    position: absolute; top: 0; left: 0; width: 1045px; height: 120px;
    display: flex; align-items: center; justify-content: center; gap: 16px;
  }
  .brand-dot { width: 46px; height: 46px; border-radius: 50%; background: var(--green); }
  .brand-name {
    font-family: "Open Sans", sans-serif; font-weight: 700; font-size: 27px;
    letter-spacing: 6px; color: var(--white);
  }

  /* Side navigation */
  .site-nav {
    position: absolute; left: 10px; top: 120px; width: 129px; height: 662px;
    border-top: 3px solid var(--white); border-bottom: 11px solid #f2f2f2;
  }
  .nav-item {
    position: absolute; left: 0; width: 129px; text-align: center;
    font-family: "Open Sans", sans-serif; font-weight: 600; font-size: 12px; color: var(--white);
    text-decoration: none;
  }
  .nav-item svg { display: block; margin: 0 auto 6px; filter: drop-shadow(0 0 5px var(--glow)); }
  .nav-item::after {
    content: ""; position: absolute; left: 28px; width: 73px; height: 8px; top: 48px;
    border-radius: 50%; background: radial-gradient(rgba(0,0,0,.35), transparent 70%);
  }

  /* Main panel */
  .page { position: absolute; left: 156px; top: 147px; width: 879px; height: 1053px; }
  .page-title {
    height: 70px; background: var(--yellow); border-radius: 8px 8px 0 0;
    font-family: "Oswald", sans-serif; font-variant: small-caps; font-size: 42px;
    color: var(--heading-ink); text-align: center; line-height: 76px; letter-spacing: .5px;
  }
  .hero { position: relative; height: 296px; background: var(--white); }
  .hero-books {
    position: absolute; left: 12px; top: 4px; width: 280px; height: 270px;
    background: radial-gradient(ellipse at 35% 40%, #6aa4df 0%, #f1d43a 30%, #dfe6ee 60%, #ffffff 80%);
  }
  .hero-team {
    position: absolute; left: 565px; top: 68px; width: 314px; height: 181px;
    background: linear-gradient(160deg, #8fc23a 0%, #6aa62a 45%, #c9a88a 75%, #5b6b7a 100%);
  }
  .hero-tagline {
    position: absolute; right: 10px; bottom: 6px;
    font-style: italic; font-size: 35px; color: var(--heading-ink);
  }

  .intro { display: flex; height: 258px; background: var(--olive); border-bottom: 2px solid var(--olive-line); }
  .video-panel { width: 385px; height: 256px; background: linear-gradient(#1a5c92, #0b3d6a); padding: 6px 8px; }
  .video-screen {
    position: relative; height: 225px; background: #000; border: 1px solid #2a7fbf;
  }
  .video-play {
    position: absolute; left: 154px; top: 96px; width: 64px; height: 36px; border-radius: 6px;
    background: linear-gradient(#d8d8d8, #8a8a8a);
  }
  .video-bar {
    position: absolute; left: 0; right: 0; bottom: 0; height: 20px;
    background: linear-gradient(#e6eef6, #9fb4c8); display: flex; align-items: center; gap: 6px; padding: 0 5px;
    font-size: 10px; color: #223;
  }
  .video-track { width: 170px; height: 5px; border-radius: 3px; background: #6c7d8e; }

  .testimonial { flex: 1; padding: 16px 20px 0 22px; }
  .section-title {
    font-family: "Oswald", sans-serif; font-variant: small-caps; font-size: 34px;
    color: var(--cream); line-height: 1;
  }
  .quote {
    margin: 14px 0 0 26px; font-style: italic; font-size: 14.5px; line-height: 25px; color: var(--quote);
  }
  .quote-author { margin: 26px 0 0 26px; font-style: italic; font-size: 19px; line-height: 23px; color: var(--white); }

  .features { background: var(--olive); height: 259px; border-bottom: 2px solid var(--olive-line); padding: 8px 0 0 23px; position: relative; }
  .features.second { height: 172px; border-bottom: 0; padding-top: 0; }
  .feature { position: absolute; width: 360px; }
  .feature-head { display: flex; align-items: center; gap: 10px; }
  .feature-title { font-style: italic; font-size: 25px; color: var(--cream); }
  .feature-text {
    margin-top: 18px; padding-left: 14px; font-style: italic; font-size: 14px; line-height: 25px;
    color: var(--white); text-align: justify;
  }
</style>
</head>
<body>

<header class="brand">
  <span class="brand-dot"></span>
  <span class="brand-name">BRIGHTLOOM WORKS</span>
</header>

<nav class="site-nav">
  <a class="nav-item" style="top:8px" href="#">
    <svg width="46" height="44" viewBox="0 0 46 44" fill="none" stroke="#ffe970" stroke-width="3" stroke-linejoin="round"><path d="M5 22 23 6l18 16"/><path d="M10 18v20h26V18"/><path d="M19 38V28h8v10"/></svg>Home</a>
  <a class="nav-item" style="top:148px" href="#">
    <svg width="46" height="44" viewBox="0 0 46 44" fill="none" stroke="#ffe970" stroke-width="3" stroke-linejoin="round"><path d="M23 4l5.5 12 13 1.3-9.8 8.8 2.9 12.9L23 32.3 11.4 39l2.9-12.9-9.8-8.8 13-1.3z"/></svg>About Us</a>
  <a class="nav-item" style="top:242px" href="#">
    <svg width="46" height="44" viewBox="0 0 46 44" fill="none" stroke="#ffe970" stroke-width="3" stroke-linejoin="round"><path d="M40 5 8 20l12 4 4 13z"/><path d="M20 24 40 5"/><path d="M6 38l8-8M4 30l5-5"/></svg>Our Services</a>
  <a class="nav-item" style="top:342px" href="#">
    <svg width="46" height="44" viewBox="0 0 46 44" fill="none" stroke="#ffe970" stroke-width="3"><circle cx="23" cy="22" r="17"/><rect x="15" y="18" width="16" height="11" rx="1"/><path d="M19 18v-3h8v3"/></svg>Portfolio</a>
  <a class="nav-item" style="top:442px" href="#">
    <svg width="46" height="44" viewBox="0 0 46 44" fill="none" stroke="#ffe970" stroke-width="3" stroke-linejoin="round"><path d="M23 5c10 0 18 6 18 14s-8 14-18 14c-2 0-4 0-6-1l-8 6 2-8c-4-3-6-7-6-11C5 11 13 5 23 5z"/><path d="M15 16h16M15 22h12"/></svg>Testimonials</a>
  <a class="nav-item" style="top:542px" href="#">
    <svg width="46" height="44" viewBox="0 0 46 44" fill="none" stroke="#ffe970" stroke-width="3" stroke-linejoin="round"><path d="M5 16c0-6 8-9 18-9s18 3 18 9l-7 2-2-5c-6-2-12-2-18 0l-2 5z"/><path d="M12 20h22l4 16H8z"/><circle cx="23" cy="28" r="4"/></svg>Contact Us</a>
</nav>

<main class="page">
  <h1 class="page-title">Course Management and Booking Simplified</h1>

  <section class="hero">
    <div class="hero-books" role="img" aria-label="Stack of colourful books with a computer mouse"></div>
    <div class="hero-team" role="img" aria-label="Team of three people at computer screens"></div>
    <p class="hero-tagline">Built with your business in mind</p>
  </section>

  <section class="intro">
    <div class="video-panel">
      <div class="video-screen">
        <svg class="video-play" viewBox="0 0 64 36"><path d="M27 11v14l12-7z" fill="#333"/></svg>
        <div class="video-bar">
          <svg width="12" height="12" viewBox="0 0 12 12"><path d="M2 1v10l9-5z" fill="#223"/></svg>
          <span class="video-track"></span>
          <span>0:00 / 0:00</span>
        </div>
      </div>
    </div>
    <div class="testimonial">
      <h2 class="section-title">Testimonial</h2>
      <p class="quote">“A convenient tool that was simple to integrate into our website. It has allowed both the business and our customers an easy way to book courses. In life sometimes simple is good and this is a great example!”</p>
      <p class="quote-author">Clara Wendell, Director @ TutorNest<br>www.tutornest.org</p>
    </div>
  </section>

  <section class="features">
    <h2 class="section-title">Key Features</h2>
    <article class="feature" style="left:23px;top:54px;width:372px">
      <div class="feature-head">
        <svg width="40" height="38" viewBox="0 0 40 38"><rect x="2" y="4" width="26" height="24" rx="2" fill="#f2f2f2" stroke="#c33" stroke-width="2"/><rect x="2" y="4" width="26" height="6" fill="#d33"/><circle cx="26" cy="25" r="11" fill="#f5a623"/><circle cx="26" cy="25" r="8" fill="#fff"/><path d="M26 19v6h4" stroke="#333" stroke-width="2" fill="none"/></svg>
        <span class="feature-title">Available and easy to use 24/7 -</span>
      </div>
      <p class="feature-text">By allowing booking and payment at any time of the day, your attendees will be more likely to commit to your event and with noaccount setup or password required and no paper forms to fill in and post, bookingonto and paying for your courses is easy.</p>
    </article>
    <article class="feature" style="left:480px;top:52px;width:356px">
      <div class="feature-head">
        <svg width="36" height="36" viewBox="0 0 36 36"><rect x="1" y="1" width="34" height="34" fill="#fff"/><rect x="5" y="6" width="26" height="18" fill="#2d6fb7" stroke="#555"/><path d="M12 29h12" stroke="#555" stroke-width="3"/><path d="M12 11l6 6" stroke="#fff" stroke-width="2"/></svg>
        <span class="feature-title">Online Course promotion</span>
      </div>
      <p class="feature-text" style="padding-left:0">List your upcoming courses in a clear and simple way so people can easily find andselect the course that suits them.</p>
    </article>
  </section>

  <section class="features second">
    <article class="feature" style="left:23px;top:10px;width:372px">
      <div class="feature-head">
        <svg width="46" height="44" viewBox="0 0 46 44"><rect x="4" y="6" width="28" height="18" rx="2" fill="#3a7bd5"/><rect x="10" y="22" width="30" height="14" rx="2" fill="#4caf50"/><ellipse cx="24" cy="38" rx="14" ry="4" fill="#7cc85a"/></svg>
        <span class="feature-title">Online &amp; Offline Payments</span>
      </div>
      <p class="feature-text">Take payments online, whilst having the flexibility of managing and adding offline payments.</p>
    </article>
    <article class="feature" style="left:480px;top:10px;width:356px">
      <div class="feature-head">
        <svg width="40" height="40" viewBox="0 0 40 40"><rect x="4" y="12" width="30" height="22" fill="#e8f0fa" stroke="#5b8fc9" stroke-width="2"/><path d="M4 12l15 12 15-12" fill="none" stroke="#5b8fc9" stroke-width="2"/><path d="M10 8c6-6 16-6 22 0l-4 1M30 38c-6 4-14 4-20 0l4-1" fill="none" stroke="#2e7bd6" stroke-width="3"/></svg>
        <span class="feature-title">Built in email system</span>
      </div>
      <p class="feature-text" style="padding-left:0">Enable quick and easy communication with upcoming course candidates and promotion of additional courses to past candidates.</p>
    </article>
  </section>
</main>

</body>
</html>
```